Design of a promotional offer flyer required to promote low-cost websites to 1-man band businesses

I want a flyer designed - either a double-sided A5 flyer or even A4 folded into a third double-sided. The flyer is to showcase a new service - low-cost websites for 1-man-band businesses, business startups and tradesmen in England. Look at the copy, find some pix and let me know! Flyer will be printed and used as an image on my website too. Pix could be related to some of the target groups. We need to stress the simple message that websites start from £5 per week and this is an-all-in-one fee.

Target Market(s)

Tradesmen, business start ups and 1-man band businesses that want a website

Industry/Entity Type

Small Business

Contact Information for Business Card

All contact details and name of business to be confirmed shortly

Font styles to use
Serif

Requirements
Must have
• Basic messages from copy for flyer i.e. websites from £5 per week and what each client gets for that price to be included on the business card! Please read copy for the flyer.
Nice to have
• Nice background image or series of small images relevant to the target audience. Again, see list of targets from copy for flyer.
Should not have
• I don't want exact or similar design to my main business Blue Harbour Promotions. The new flyer and business card should be a different and distinct branding to that of Blue Harbour Promotions. Aimed at a more economical style, whilst looking professional, but relevant to the target audiences.

```html
<!DOCTYPE html>
<html lang="en">
<head>
<meta charset="utf-8">
<title>Low-Cost Websites Flyer</title>
<link rel="stylesheet" href="https://fonts.googleapis.com/css2?family=Bebas+Neue&family=Open+Sans:wght@400;700&family=Arimo:wght@700&display=swap">
<style>
  :root {
    --page-bg: #f2f2f2;
    --paper: #ffffff;
    --brand-blue: #5b9ac4;
    --brand-blue-deep: #3f7fae;
    --tag-blue: #a9d0ea;
    --tag-grey: #e9e9e9;
    --tag-dark: #2f2f2f;
    --gold: #e2b92c;
    --gold-light: #f7dc6a;
    --ink: #222222;
    --headline-blue: #4f8fc0;
    --white: #ffffff;
  }
  * { margin: 0; padding: 0; box-sizing: border-box; }
  html, body { width: 846px; height: 1200px; overflow: hidden; background: var(--page-bg); }
  .canvas { position: relative; width: 846px; height: 1200px; }

  .flyer {
    position: absolute; left: 33px; top: 327px;
    width: 706px; height: 493px;
    background: var(--paper);
    transform: scale(1.105); transform-origin: top left;
    overflow: hidden;
    box-shadow: 0 2px 6px rgba(0,0,0,0.08);
  }

  .photo { position: absolute; }
  .photo--makeup { left: 16px; top: 40px; width: 160px; height: 113px; background: linear-gradient(135deg, #8a5a3c, #c9a27a 55%, #3a2a20); z-index: 2; }
  .photo--painting { left: 116px; top: 13px; width: 166px; height: 120px; background: linear-gradient(90deg, #b07a45, #d6a46a 50%, #9c6a3a); z-index: 1; }
  .photo--engraver { left: 73px; top: 153px; width: 139px; height: 107px; background: linear-gradient(135deg, #ece8e4, #b9a89a 50%, #4c4a4a); z-index: 2; }
  .photo--photographer { left: 238px; top: 112px; width: 125px; height: 186px; background: linear-gradient(160deg, #d9d9d9, #555555 55%, #1a1a1a); z-index: 2; }

  .photo--desk {
    left: 0; top: 280px; width: 383px; height: 213px;
    background: linear-gradient(180deg, #ffffff 0%, #f1f1f1 60%, #e4e4e4 100%);
  }

  .screen {
    position: absolute; left: 17px; top: 270px; width: 208px; height: 120px;
    background: var(--paper);
    border: 5px solid #111111;
    border-radius: 3px;
    text-align: center;
    padding-top: 12px;
    z-index: 3;
  }
  .screen::after {
    content: ""; position: absolute; left: -5px; right: -5px; bottom: -20px; height: 15px;
    background: linear-gradient(180deg, #d8d8d8, #bdbdbd); border-radius: 0 0 4px 4px;
  }
  .screen__title {
    font-family: "Bebas Neue", sans-serif; font-size: 21px; line-height: 25px;
    color: var(--headline-blue); letter-spacing: 0.2px;
  }
  .screen__text {
    font-family: "Open Sans", sans-serif; font-size: 13px; line-height: 18px;
    color: var(--ink); margin-top: 6px;
  }

  .panel {
    position: absolute; left: 383px; top: 0; width: 323px; height: 493px; z-index: 4;
    background: var(--brand-blue);
    border-left: 4px solid var(--brand-blue-deep);
  }

  .headline {
    position: absolute; left: 399px; width: 300px; top: 40px; z-index: 5;
    font-family: "Bebas Neue", sans-serif; font-size: 34px; line-height: 36px;
    color: var(--white); text-align: center; letter-spacing: 0.3px;
  }

  .price-badge {
    position: absolute; left: 488px; top: 180px; width: 136px; height: 136px; z-index: 5;
    border-radius: 50%;
    background: radial-gradient(circle at 40% 35%, var(--gold-light), var(--gold) 70%, #c99b1a);
    border: 3px dotted var(--gold-light);
    text-align: center; color: var(--white);
    font-family: "Bebas Neue", sans-serif;
  }
  .price-badge__amount { display: block; font-size: 58px; line-height: 58px; margin-top: 16px; }
  .price-badge__label { display: block; font-size: 24px; line-height: 24px; }

  .contact-tag {
    position: absolute; z-index: 5;
    font-family: "Arimo", sans-serif; font-weight: 700;
    display: flex; align-items: center; justify-content: center;
    white-space: nowrap;
  }
  .contact-tag--phone {
    left: 470px; top: 357px; width: 207px; height: 36px;
    background: var(--tag-blue); color: var(--white); font-size: 23px; letter-spacing: 0.5px;
    clip-path: polygon(8% 0, 100% 0, 92% 100%, 0 100%);
  }
  .contact-tag--web {
    left: 418px; top: 395px; width: 234px; height: 36px;
    background: var(--tag-grey); color: var(--ink); font-size: 15px;
    clip-path: polygon(0 0, 92% 0, 100% 100%, 6% 100%);
  }
  .contact-tag--email {
    left: 462px; top: 432px; width: 234px; height: 36px;
    background: var(--tag-dark); color: var(--white); font-size: 15px;
    clip-path: polygon(7% 0, 100% 0, 94% 100%, 0 100%);
  }
</style>
</head>
<body>
<main class="canvas">
  <article class="flyer">
    <div class="photo photo--desk" role="img" aria-label="Bright white desk with computer, keyboard, lamp and pen pot"></div>
    <div class="photo photo--painting" role="img" aria-label="Paintbrush painting a wooden surface blue"></div>
    <div class="photo photo--makeup" role="img" aria-label="Make-up artist working on a client"></div>
    <div class="photo photo--engraver" role="img" aria-label="Craftsman with magnifying glasses working on a small ring"></div>
    <div class="photo photo--photographer" role="img" aria-label="Black and white portrait of a photographer holding a camera"></div>

    <div class="screen">
      <h2 class="screen__title">Professionally-Designed<br>Websites</h2>
      <p class="screen__text">only £5 per week and no<br>upfront costs!</p>
    </div>

    <div class="panel" aria-hidden="true"></div>

    <h1 class="headline">For Tradesmen, Business<br>Start-ups and 1-Man<br>Bands</h1>

    <div class="price-badge">
      <span class="price-badge__amount">£5</span>
      <span class="price-badge__label">All in one<br>fee</span>
    </div>

    <p class="contact-tag contact-tag--phone">0161-555-0142</p>
    <p class="contact-tag contact-tag--web">www.smallsitestudio.co.uk</p>
    <p class="contact-tag contact-tag--email">hello@smallsitestudio.co.uk</p>
  </article>
</main>
</body>
</html>
```